Luxury Brand Coffee Table Book Template

Overview:
We are creating a premium, 28-page coffee table book to accompany every bespoke jewelry piece handcrafted by Vellmoor Jewelry. This book serves as an heirloom that documents the story, design, and craftsmanship behind each custom piece, culminating in a powerful legacy statement. We need a refined, luxurious, and masculine layout template that can be updated for each new customer.
**All reference files (images, logos, copy for pages, etc.) are included in the .zip file.
Deliverables:
Print-ready 28-page InDesign or editable template file
Front and back cover design
Consistent typography and page layouts based on our outlined structure
Design system that allows for easy photo and text updates per client
Specs:
Size: 8.1 x 10.6 in, Portrait Orientation
Cover: Black linen hardcover with gold foil stamped name or crest (simulated in mockup)
Interior: Deep matte photo paper feel – minimalistic, clean layout with generous whitespace
Color Palette: Black, white, and gold
Style: Bold, masculine, timeless, high-luxury (think Karvane Studio x Dellbrook & Co.)
See the attached 28-page outline. Please use stock image placeholders for now.
Target Market(s)
Affluent Men & Women age 35-65
Industry/Entity Type
Luxury Retail Jewelry
Font styles to use
Other font styles liked:
- I really like Trajan Pro 3, but open to suggestions, as well as a mixture of Serif and Sans Serif fonts
Look and feel
Each slider illustrates characteristics of the customer's brand and the style your logo design should communicate.

```html
<!DOCTYPE html>
<html lang="en">
<head>
<meta charset="utf-8">
<title>Vellmoor Jewelry — Coffee Table Book Spreads</title>
<link rel="stylesheet" href="https://fonts.googleapis.com/css2?family=Cinzel:wght@400;600&family=Lato:wght@400;700&family=Great+Vibes&display=swap">
<style>
  :root {
    --backdrop: #6b6b6b;
    --page: #0d0d0f;
    --gold: #c9a24a;
    --gold-light: #e8c872;
    --text: #a9a9ad;
    --white: #f2f2f2;
  }
  * { margin: 0; padding: 0; box-sizing: border-box; }
  html, body { width: 699px; height: 1200px; overflow: hidden; }
  body {
    background: radial-gradient(ellipse at center, #7a7a7a 0%, var(--backdrop) 100%);
    font-family: "Lato", Arial, sans-serif;
  }
  .spreads {
    display: grid;
    grid-template-columns: 290px 290px;
    grid-template-rows: repeat(3, 375px);
    gap: 22px 29px;
    padding: 15px 0 0 45px;
  }
  .page {
    position: relative;
    background: var(--page);
    overflow: hidden;
    box-shadow: 0 4px 10px rgba(0,0,0,.45);
  }
  .folio {
    position: absolute; right: 10px; bottom: 9px;
    width: 7px; height: 7px; background: var(--gold);
  }
  .body-copy {
    font-size: 4.6px; line-height: 1.65; color: var(--text);
  }
  .body-copy p + p { margin-top: 5px; }
  .heading {
    font-family: "Cinzel", "Times New Roman", serif;
    color: var(--gold-light);
    letter-spacing: .5px;
  }
  .rule { height: 1px; background: linear-gradient(90deg, var(--gold), rgba(201,162,74,.15)); }
  .subhead {
    font-size: 5px; font-weight: 700; color: var(--white);
    letter-spacing: .5px; text-transform: uppercase; margin: 7px 0 4px;
  }

  /* Cover */
  .cover-sheen {
    position: absolute; inset: 0;
    background:
      linear-gradient(155deg, rgba(201,162,74,.55) 0%, rgba(201,162,74,0) 32%),
      linear-gradient(165deg, rgba(0,0,0,0) 10%, rgba(232,200,114,.35) 18%, rgba(0,0,0,0) 26%),
      linear-gradient(140deg, rgba(0,0,0,0) 20%, rgba(201,162,74,.25) 27%, rgba(0,0,0,0) 34%);
  }
  .brand {
    position: absolute; top: 165px; left: 0; right: 0;
    display: flex; align-items: center; justify-content: center; gap: 7px;
  }
  .brand-mark { width: 18px; height: 18px; border-radius: 50%; background: var(--gold); }
  .brand-name {
    font-family: "Cinzel", serif; font-weight: 600; font-size: 15px;
    color: var(--gold-light); letter-spacing: 1px; text-transform: uppercase;
  }
  .cover-rule { position: absolute; top: 198px; left: 40px; right: 40px; }
  .cover-title {
    position: absolute; top: 210px; left: 0; right: 0; text-align: center;
    font-size: 17px; line-height: 1.45;
  }

  /* Story */
  .story { padding: 18px 16px; }
  .story .heading { font-size: 14px; margin-bottom: 5px; }
  .note { display: flex; gap: 10px; }
  .note .body-copy { flex: 1; }
  .portrait { width: 70px; height: 80px; background: linear-gradient(160deg, #4a4a4e, #1e1e22); flex: none; margin-top: 4px; }
  .signature {
    position: absolute; right: 22px; bottom: 40px;
    font-family: "Great Vibes", cursive; color: var(--white); font-size: 17px;
  }

  /* Ring */
  .ring-photo {
    position: absolute; inset: 0;
    background: radial-gradient(ellipse 55% 45% at 50% 45%, #8a6a2a 0%, #4a3516 40%, #0d0d0f 75%);
  }

  /* Narrative */
  .narrative { padding: 18px 16px; }
  .narrative .heading { font-size: 14px; margin-bottom: 5px; }
  .columns { display: grid; grid-template-columns: 1fr 1fr; gap: 12px; margin-top: 8px; }
  .quote {
    position: absolute; left: 0; right: 0; top: 270px; text-align: center;
    font-family: "Great Vibes", cursive; color: var(--gold-light);
    font-size: 22px; line-height: 1.3;
  }
  .quote-rule { position: absolute; top: 262px; left: 30px; right: 30px; }

  /* Stone setting */
  .flame-photo {
    position: absolute; top: 0; left: 0; right: 0; height: 205px;
    background: radial-gradient(ellipse 45% 55% at 60% 60%, #f0a23a 0%, #a4521a 35%, #2a1408 70%, #0d0d0f 100%);
  }
  .technique-title {
    position: absolute; top: 14px; left: 16px; font-size: 15px; line-height: 1.3;
  }
  .three-col {
    position: absolute; top: 225px; left: 16px; right: 16px;
    display: grid; grid-template-columns: repeat(3, 1fr); gap: 10px;
  }

  /* Craft */
  .hands-photo {
    position: absolute; top: 0; left: 0; right: 0; height: 170px;
    background: linear-gradient(135deg, #3a2a1e 0%, #7a5a3e 45%, #b48a62 60%, #2a1e16 100%);
  }
  .craft-copy { position: absolute; top: 185px; left: 16px; right: 16px; }
</style>
</head>
<body>
<main class="spreads">

  <section class="page cover">
    <div class="cover-sheen"></div>
    <div class="brand">
      <span class="brand-mark"></span>
      <span class="brand-name">Vellmoor Jewelry</span>
    </div>
    <div class="rule cover-rule"></div>
    <h1 class="heading cover-title">A Timeless<br>Companion to Every<br>Custom Creation</h1>
  </section>

  <section class="page story">
    <h2 class="heading">Story</h2>
    <div class="rule"></div>
    <div class="subhead">Customer's Story</div>
    <div class="body-copy">
      <p>Every piece begins with a conversation about the people, places and moments that matter most. From that first meeting we shape the metal, choose the stones and record the journey here.</p>
      <p>Every piece begins with a conversation about the people, places and moments that matter most. From that first meeting we shape the metal, choose the stones and record the journey here.</p>
    </div>
    <div class="subhead">Personal Note from Designer</div>
    <div class="note">
      <div class="body-copy">
        <p>Every piece begins with a conversation about the people, places and moments that matter most. From that first meeting we shape the metal, choose the stones and record the journey here.</p>
        <p>Every piece begins with a conversation about the people, places and moments that matter most. From that first meeting we shape the metal, choose the stones and record the journey here.</p>
      </div>
      <div class="portrait" role="img" aria-label="Portrait photo of the designer"></div>
    </div>
    <div class="signature">John Doe</div>
    <span class="folio"></span>
  </section>

  <section class="page">
    <div class="ring-photo" role="img" aria-label="Photo of a gold signet ring with a blue stone on black"></div>
  </section>

  <section class="page narrative">
    <h2 class="heading">Narrative Text</h2>
    <div class="rule"></div>
    <div class="columns">
      <div class="body-copy">
        <p>Every piece begins with a conversation about the people, places and moments that matter most. From that first meeting we shape the metal, choose the stones and record the journey here.</p>
        <p>Every piece begins with a conversation about the people, places and moments that matter most. From that first meeting we shape the metal, choose the stones and record the journey here.</p>
        <p>Every piece begins with a conversation about the people, places and moments that matter most. From that first meeting we shape the metal, choose the stones and record the journey here.</p>
      </div>
      <div class="body-copy">
        <p>Every piece begins with a conversation about the people, places and moments that matter most. From that first meeting we shape the metal, choose the stones and record the journey here.</p>
        <p>Every piece begins with a conversation about the people, places and moments that matter most. From that first meeting we shape the metal, choose the stones and record the journey here.</p>
        <p>Every piece begins with a conversation about the people, places and moments that matter most. From that first meeting we shape the metal, choose the stones and record the journey here.</p>
      </div>
    </div>
    <div class="rule quote-rule"></div>
    <p class="quote">Jewelry is Memory<br>Made Tangible.</p>
    <span class="folio"></span>
  </section>

  <section class="page">
    <div class="flame-photo" role="img" aria-label="Photo of a jeweler's torch flame during stone setting"></div>
    <h2 class="heading technique-title">Stone Setting<br>Technique</h2>
    <div class="three-col">
      <div class="body-copy"><p>Every piece begins with a conversation about the people, places and moments that matter most. From that first meeting we shape the metal, choose the stones and record the journey here.</p></div>
      <div class="body-copy"><p>Every piece begins with a conversation about the people, places and moments that matter most. From that first meeting we shape the metal, choose the stones and record the journey here.</p></div>
      <div class="body-copy"><p>Every piece begins with a conversation about the people, places and moments that matter most. From that first meeting we shape the metal, choose the stones and record the journey here.</p></div>
    </div>
    <span class="folio"></span>
  </section>

  <section class="page">
    <div class="hands-photo" role="img" aria-label="Photo of a craftsman's hands working on a ring"></div>
    <div class="body-copy craft-copy">
      <p>Every piece begins with a conversation about the people, places and moments that matter most. From that first meeting we shape the metal, choose the stones and record the journey here.</p>
      <p>Every piece begins with a conversation about the people, places and moments that matter most. From that first meeting we shape the metal, choose the stones and record the journey here.</p>
      <p>Every piece begins with a conversation about the people, places and moments that matter most. From that first meeting we shape the metal, choose the stones and record the journey here.</p>
    </div>
    <span class="folio"></span>
  </section>

</main>
</body>
</html>
```